Pruett Family Motto/Mission Statement

We are creating a poster to be hung in our home with several purpose statements for our family (last name Pruett, and "The Pruett Family" should be included in the poster prominently). The text that we want included is in the attached file.

Our kids range in age from 8 to 17, so we are looking for something that is homey and cheerful, but fairly bold and oriented to older kids (and not so much younger kids).

I've attached a couple of example poster/statements that we generally like. Overall color scheme could include blues and greens and possibly some brown.

Anticipated size of this poster would be 18"x24" with a portrait orientation.

```html
<!DOCTYPE html>
<html lang="en">
<head>
<meta charset="utf-8">
<title>The Pruett Family – Family Mission Poster</title>
<link rel="stylesheet" href="https://fonts.googleapis.com/css2?family=Tinos&family=Michroma&display=swap">
<style>
  :root {
    --page-bg: #1e1e20;
    --poster-violet: #4a4cc2;
    --poster-blue: #3f5fd0;
    --glow-teal: #1f9fb4;
    --glow-green: #2f9a6a;
    --art-green: #2c7d55;
    --art-brown: #5a3a2c;
    --text-light: #f2f4f8;
    --accent-lime: #c9e33c;
    --accent-cyan: #52cde8;
    --title-teal: #0f4f60;
    --title-edge: #3fd2e4;
  }
  * { margin: 0; padding: 0; box-sizing: border-box; }
  html, body {
    width: 1200px; height: 750px; overflow: hidden;
    background: var(--page-bg);
  }
  .stage {
    position: relative; width: 1200px; height: 750px;
  }
  .poster {
    position: absolute; left: 330px; top: 15px;
    width: 540px; height: 720px; overflow: hidden;
    background:
      radial-gradient(ellipse 55% 50% at 50% 50%, var(--glow-teal) 0%, var(--poster-blue) 60%, var(--poster-violet) 100%);
  }
  .poster__art {
    position: absolute; left: 20px; top: 0; width: 500px; height: 690px;
    background:
      radial-gradient(ellipse 38% 22% at 58% 18%, rgba(44,125,85,0.75) 0%, rgba(44,125,85,0) 100%),
      radial-gradient(ellipse 18% 20% at 20% 76%, rgba(140,200,80,0.55) 0%, rgba(47,154,106,0) 100%),
      radial-gradient(ellipse 18% 20% at 78% 76%, rgba(140,200,80,0.55) 0%, rgba(47,154,106,0) 100%),
      radial-gradient(ellipse 10% 12% at 12% 62%, rgba(90,58,44,0.5) 0%, rgba(90,58,44,0) 100%),
      radial-gradient(ellipse 10% 12% at 40% 86%, rgba(90,58,44,0.5) 0%, rgba(90,58,44,0) 100%);
  }
  .poster__side-title {
    position: absolute; left: 14px; top: 24px;
    writing-mode: vertical-rl; transform: rotate(180deg);
    font-family: "Michroma", sans-serif; font-size: 10px; letter-spacing: 1.5px;
    color: var(--text-light);
  }
  .values {
    position: absolute; left: 0; top: 0; width: 100%; list-style: none;
    font-family: "Tinos", serif; color: var(--text-light); font-size: 16px;
  }
  .values__item {
    position: absolute; left: 0; width: 100%; text-align: center; line-height: 1;
  }
  .values__key { font-size: 22px; }
  .values__key--lime { color: var(--accent-lime); }
  .values__key--cyan { color: var(--accent-cyan); }
  .poster__title {
    position: absolute; left: 0; width: 100%; top: 652px; text-align: center;
    font-family: "Michroma", sans-serif; font-size: 27px; letter-spacing: 2px;
    color: var(--title-teal);
    -webkit-text-stroke: 0.7px var(--title-edge);
  }
</style>
</head>
<body>
<main class="stage">
  <article class="poster">
    <div class="poster__art" role="img" aria-label="Illustration of flowing translucent ribbons above silhouettes of children cartwheeling and leaping, in greens, teals and browns"></div>
    <p class="poster__side-title">THE PRUETT FAMILY</p>
    <ul class="values">
      <li class="values__item" style="top:146px">We love to <span class="values__key values__key--lime">learn</span> new things.</li>
      <li class="values__item" style="top:206px">We look at life through a <span class="values__key values__key--cyan">positive</span> lens.</li>
      <li class="values__item" style="top:266px"><span class="values__key values__key--lime">Kindness</span> guides our words and deeds.</li>
      <li class="values__item" style="top:326px">We create <span class="values__key values__key--cyan">adventure</span> and choose experiences over things.</li>
      <li class="values__item" style="top:386px">We commit to be <span class="values__key values__key--lime">fit.</span></li>
      <li class="values__item" style="top:446px">Our days are brightened by a <span class="values__key values__key--cyan">sense of humor.</span></li>
      <li class="values__item" style="top:506px">We <span class="values__key values__key--lime">do what is right</span> even when no one is watching.</li>
    </ul>
    <h1 class="poster__title">THE PRUETT FAMILY</h1>
  </article>
</main>
</body>
</html>
```